Designing our 2018 Look Book! New help with slide design and picture layout

We create a yearly "Look book" with all of our season's designs for the year and need creative help creating the design and layout of the book

Need help with the slide design and picture layout

Target Market(s)

Property managers and office managers

Requirements
Must have
• layout of the photos and design of cover slide templates
• See our logo attached (color scheme and you can use the logo as well)
• Also see our website for our "look" www.dunvoria.com

```html
<!DOCTYPE html>
<html lang="en">
<head>
<meta charset="utf-8">
<title>Dunvoria Look Book – Spread</title>
<link href="https://fonts.googleapis.com/css2?family=Open+Sans:wght@400;600;700&display=swap" rel="stylesheet">
<style>
  :root {
    --backdrop: #ecebe7;
    --paper: #f4f4f2;
    --paper-shade: #e4e4e2;
    --ink: #3a3a3a;
    --leaf-green: #5c9b2c;
    --foliage-dark: #2f5a1e;
    --foliage-light: #7fb347;
    --lobby-dark: #1d2230;
    --lobby-warm: #8a6a45;
    --white: #ffffff;
  }
  * { box-sizing: border-box; margin: 0; padding: 0; }
  html, body { width: 1200px; height: 800px; overflow: hidden; }
  body {
    background: var(--backdrop);
    font-family: "Open Sans", Arial, sans-serif;
    color: var(--ink);
  }
  .spread {
    position: absolute;
    left: 40px; top: 170px;
    width: 1120px; height: 460px;
    display: flex;
    box-shadow: 0 12px 30px rgba(0,0,0,0.18);
  }
  .page {
    position: relative;
    width: 560px; height: 460px;
    background: var(--paper);
    overflow: hidden;
  }
  .page--left { background: linear-gradient(90deg, var(--paper) 80%, var(--paper-shade)); }
  .page--right { background: linear-gradient(90deg, var(--paper-shade), var(--paper) 20%); }
  .page__art { position: absolute; inset: 0; width: 100%; height: 100%; }
  .wordmark {
    position: absolute;
    display: flex; align-items: center; gap: 8px;
    color: var(--white);
    font-size: 24px; font-weight: 400;
    letter-spacing: 0.5px;
  }
  .wordmark__dot { width: 12px; height: 12px; border-radius: 50%; background: var(--white); }
  .wordmark--left { left: 28px; top: 26px; }
  .wordmark--right { right: 24px; top: 232px; }
  .section-title {
    position: absolute;
    color: var(--leaf-green);
    font-size: 15px; font-weight: 600;
  }
  .copy {
    position: absolute;
    font-size: 9.5px; line-height: 1.5;
  }
  .copy strong { font-weight: 700; }
  .page--left .section-title { left: 30px; top: 192px; }
  .page--left .copy--lead { left: 30px; top: 218px; width: 235px; }
  .page--left .copy--side { left: 300px; top: 330px; width: 235px; }
  .page--right .section-title { left: 26px; top: 170px; }
  .page--right .copy--lead { left: 26px; top: 196px; width: 250px; }
  .page--right .copy--side { left: 295px; top: 340px; width: 245px; }
</style>
</head>
<body>
  <main class="spread">
    <section class="page page--left">
      <svg class="page__art" viewBox="0 0 560 460" aria-hidden="false">
        <defs>
          <linearGradient id="foliage" x1="0" y1="0" x2="1" y2="1">
            <stop offset="0" stop-color="var(--foliage-dark)"/>
            <stop offset="0.6" stop-color="#4c7f2a"/>
            <stop offset="1" stop-color="var(--foliage-light)"/>
          </linearGradient>
          <linearGradient id="floor" x1="0" y1="0" x2="1" y2="1">
            <stop offset="0" stop-color="#2a2a2a"/>
            <stop offset="1" stop-color="#6a6a6a"/>
          </linearGradient>
        </defs>
        <path role="img" aria-label="Photo of a lush living green wall in an office"
              d="M0 0 H560 V330 C470 240 300 175 0 170 Z" fill="url(#foliage)"/>
        <path role="img" aria-label="Photo of a dark stone lobby floor"
              d="M0 370 C90 380 170 420 220 460 H0 Z" fill="url(#floor)"/>
      </svg>
      <div class="wordmark wordmark--left"><span class="wordmark__dot"></span>Dunvoria</div>
      <h2 class="section-title">Corporate Campuses + Large Offices</h2>
      <p class="copy copy--lead"><strong>A beautiful, healthy plant program</strong> makes your brand more engaging and competitive, and our proprietary cloud platform allows us to create, maintain and refresh branded plant programs at scale across campuses with complete accountability and inventory transparency.</p>
      <p class="copy copy--side">Working with Dunvoria, you can expect consistency in design across all your green spaces. We are one of the largest interior plant providers, serving many of the Harbor Region's best-known global companies who track their plant programs by cost center with real-time access to online inventories.</p>
    </section>
    <section class="page page--right">
      <svg class="page__art" viewBox="0 0 560 460">
        <defs>
          <linearGradient id="lobby" x1="0" y1="0" x2="1" y2="0.6">
            <stop offset="0" stop-color="#3a4a6a"/>
            <stop offset="0.45" stop-color="var(--lobby-warm)"/>
            <stop offset="1" stop-color="var(--lobby-dark)"/>
          </linearGradient>
        </defs>
        <path role="img" aria-label="Photo of a bright glass-walled office lobby with columns and plants"
              d="M0 0 H560 V330 C430 300 220 160 0 140 Z" fill="url(#lobby)"/>
      </svg>
      <div class="wordmark wordmark--right"><span class="wordmark__dot"></span>Dunvoria</div>
      <h2 class="section-title">Property Managers</h2>
      <p class="copy copy--lead">From tenant needs and occupancy fluctuations to keeping a handle on operating expenses, we know you have many demands on your hands. A Dunvoria plant program offers a high-impact, low-cost amenity that differentiates your property and enhances its value, while keeping your tenants happy and attracting prospective tenants.</p>
      <p class="copy copy--side">We know how to keep your Class A office space looking that way with design, installation and ongoing service — all while giving you full transparency and 24/7 online visibility into your plant program inventory. And with a cornucopia of holiday decor, we can transform any lobby into a spectacular winter dreamscape.</p>
    </section>
  </main>
</body>
</html>
```